MT Halloway Insurance - Aviation

We are wanting to have new business cards designed for our new aviation division. We currently have business cards for the other business (attached). We would like to use the same colors and have the logo somewhere on the business card along with a small, single engine airplane, maybe in the background but would like it to be different than the original and more focused on aviation. Also wondering if there is a way to do laser cut and make the business card in the shape of an airplane? Just some different ideas that make it stand out.

Target Market(s)

Pilots

Industry/Entity Type

Insurance

Contact Information for Business Card

We would like to use the same colors and have the logo somewhere on the business card along with a small, single engine airplane, maybe in the background but would like it to be different than the original and more focused on aviation. Also wondering if there is a way to do laser cut and make the business card in the shape of an airplane? Just some different ideas that make it stand out.

Requirements
Must have
• A small, single engine airplane

```html
<!DOCTYPE html>
<html lang="en">
<head>
<meta charset="UTF-8">
<title>MT Halloway Insurance – Business Cards</title>
<link rel="stylesheet" href="https://fonts.googleapis.com/css2?family=Cinzel:wght@400;600&family=Montserrat:wght@400;500&display=swap">
<style>
  :root {
    --bg: #c9c9c9;
    --card-dark: #262626;
    --card-light: #eceef2;
    --brand-red: #d4164f;
    --ink-grey: #4a4a4c;
    --line-silver: #bdbdbd;
    --text-light: #f2f2f2;
    --sky-top: #a9cbea;
    --sky-bottom: #e7ebf1;
  }
  * { box-sizing: border-box; margin: 0; padding: 0; }
  html, body { width: 1200px; height: 800px; overflow: hidden; }
  body {
    background: var(--bg);
    font-family: "Montserrat", sans-serif;
    position: relative;
  }
  .card {
    position: absolute;
    top: 245px;
    width: 530px;
    height: 303px;
    overflow: hidden;
    border-bottom: 3px solid var(--brand-red);
  }
  /* Back of card: contact side */
  .card--contact {
    left: 50px;
    background: var(--card-dark);
    color: var(--text-light);
  }
  .contact__brand {
    position: absolute;
    left: 40px; top: 44px;
    display: flex; align-items: center; gap: 10px;
    font-family: "Cinzel", serif;
    font-weight: 400;
    font-size: 17px;
    letter-spacing: 1px;
    color: var(--text-light);
  }
  .contact__brand-dot {
    width: 12px; height: 12px; border-radius: 50%;
    background: var(--brand-red);
  }
  .contact__rule {
    position: absolute;
    left: 40px; right: 40px;
    height: 1px;
    background: linear-gradient(90deg, transparent, var(--line-silver), transparent);
  }
  .contact__rule--top { top: 88px; }
  .contact__rule--bottom { top: 232px; }
  .contact__person {
    position: absolute;
    left: 40px; top: 112px;
  }
  .contact__name {
    font-family: "Cinzel", serif;
    font-size: 24px;
    color: var(--brand-red);
    letter-spacing: 0.5px;
  }
  .contact__title {
    font-size: 13px;
    margin-top: 4px;
    letter-spacing: 0.5px;
  }
  .contact__details {
    position: absolute;
    left: 290px; top: 104px;
    list-style: none;
    font-size: 11.5px;
    line-height: 1.55;
  }
  .contact__details li { display: flex; gap: 8px; align-items: flex-start; }
  .contact__details svg { flex: none; margin-top: 3px; }
  .contact__web {
    position: absolute;
    left: 0; right: 0; top: 252px;
    text-align: center;
    font-size: 12px;
    letter-spacing: 6px;
  }
  /* Front of card: brand side */
  .card--brand {
    left: 620px;
    background: linear-gradient(200deg, var(--sky-top) 0%, var(--sky-bottom) 45%, var(--card-light) 100%);
  }
  .brand__plane {
    position: absolute;
    right: 40px; top: 24px;
    width: 170px; height: 70px;
    border-radius: 35px;
    background: radial-gradient(ellipse at center, #f7f8fb 0%, #c9d3de 60%, rgba(201,211,222,0) 100%);
  }
  .brand__mark {
    position: absolute;
    left: 0; right: 0; top: 128px;
    display: flex; justify-content: center; align-items: center; gap: 12px;
  }
  .brand__dot {
    width: 16px; height: 16px; border-radius: 50%;
    background: var(--brand-red);
  }
  .brand__name {
    font-family: "Cinzel", serif;
    font-weight: 400;
    font-size: 30px;
    color: var(--ink-grey);
    letter-spacing: 1px;
  }
  .brand__rule {
    position: absolute;
    left: 70px; right: 70px; top: 180px;
    height: 1px;
    background: linear-gradient(90deg, transparent, var(--ink-grey), transparent);
  }
  .brand__web {
    position: absolute;
    left: 0; right: 0; top: 215px;
    text-align: center;
    font-family: "Cinzel", serif;
    font-size: 15px;
    letter-spacing: 5px;
    color: var(--brand-red);
  }
</style>
</head>
<body>
  <section class="card card--contact">
    <div class="contact__brand"><span class="contact__brand-dot"></span>MT Halloway Insurance</div>
    <div class="contact__rule contact__rule--top"></div>
    <div class="contact__person">
      <p class="contact__name">Daniel Halloway</p>
      <p class="contact__title">Principal Agent</p>
    </div>
    <ul class="contact__details">
      <li>
        <svg width="10" height="12" viewBox="0 0 10 12"><path d="M5 0a4 4 0 0 1 4 4c0 3-4 8-4 8S1 7 1 4a4 4 0 0 1 4-4z" fill="#d4164f"/><circle cx="5" cy="4" r="1.5" fill="#262626"/></svg>
        <span>482 Meadow Parkway<br>Brandon, Texas 75011</span>
      </li>
      <li>
        <svg width="10" height="10" viewBox="0 0 10 10"><path d="M2 0l2 2.5-1 1.5a6 6 0 0 0 3 3l1.5-1L10 8l-1.5 2C4 10 0 6 0 1.5z" fill="#d4164f"/></svg>
        <span>555-310-2741</span>
      </li>
      <li>
        <svg width="10" height="12" viewBox="0 0 10 12"><rect x="1" y="0.5" width="8" height="11" rx="1.5" fill="none" stroke="#f2f2f2"/></svg>
        <span>555 318 6620</span>
      </li>
      <li>
        <svg width="11" height="8" viewBox="0 0 11 8"><rect width="11" height="8" fill="#d4164f"/><path d="M0 0l5.5 4.5L11 0" fill="none" stroke="#262626"/></svg>
        <span>daniel@mthins.com</span>
      </li>
    </ul>
    <div class="contact__rule contact__rule--bottom"></div>
    <p class="contact__web">WWW.MTHINS.COM</p>
  </section>

  <section class="card card--brand">
    <div class="brand__plane" role="img" aria-label="Photo of a small white single engine airplane in flight"></div>
    <div class="brand__mark"><span class="brand__dot"></span><span class="brand__name">MT Halloway Insurance</span></div>
    <div class="brand__rule"></div>
    <p class="brand__web">WWW.MTHINS.COM</p>
  </section>
</body>
</html>
```